Social Media Tool / Marketing Tool homepage design

We need a design template for a website to promote a web based technology / service. The product provide companies with a tools to generate business from social media web site.

We would like a homepage designed and an inner page of the site. This can be a contact us page or a sign up screen... Would also be good to have a design for the blog page of the site and static page i.e affiliates or advertiser page.

The feel of the site should reflect the fact that this is a social media tool but should not be too casual as we will have business clients so a blend between informal, practical and should communicate to business people (professional marketers)

Site should look friendly, thinking rounded edges rather than squared.

We have included logo design and like the idea of using the haxagonal shapes on the background in some way... Also included link to black on black design mock up that's not right as it's too heavy and does not appeal to any of the women we have shown it to. (50% of our audience)

http://mockups.brindlevault-studio.example/ORB/showcase/html/mockup3.html

http://mockups.brindlevault-studio.example/ORB/showcase/html/mockup1_2.html

http://mockups.brindlevault-studio.example/ORB/showcase/html/inner-page1.html

Above link to design that's not right. The taxonomy is right just not the black on black design. We are happy to use black but not black on a black background.

Please consider that we have 4 user types we are trying to sell to on this page hence the 4 blocks on the homepage. Feel free to interparate this how you will could be good as hexagons? or blocks??

Have attached a powerpoint of site pages please take homepage and dummy content and sign up / form page or contact page.

I have also attached logos please only use logo with one coloured hexagon the other file (logo) does not have the hexagon coloured but does include a set of icons that could also be used.

logo font = Metrostyle extended

Target Market(s)

Young professional marketers at bluechip businesses. User of social media sites like pormbly / quillnest and chirvo.

Industry/Entity Type

Business

Requirements
Must have
• should include pormbly, chirvo and quillnest icons (these will link to our profiles on these sites) Should feel friendly yet established, should feel social as this is a tool to market via social media. rounded edges / corners.
Should not have
• not old style fonts not fonts like times roman .. no squared (hard) corners.

```html
<!DOCTYPE html>
<html lang="en">
<head>
<meta charset="utf-8">
<title>Vela-Q-Gauge — Advocacy Marketing Platform</title>
<link href="https://fonts.googleapis.com/css2?family=Arimo:wght@400;700&family=Michroma&display=swap" rel="stylesheet">
<style>
:root{
  --bg:#121314;
  --bar:#2b2d31;
  --orange:#e8561a;
  --orange-light:#f47a32;
  --orange-dark:#c9410d;
  --white:#ffffff;
  --panel:#f4f5f7;
  --text:#6b6e73;
  --muted:#9a9da2;
  --nav:#a3a6ab;
  --black:#0b0b0c;
}
*{box-sizing:border-box;margin:0;padding:0}
html,body{width:1016px;height:1200px;overflow:hidden}
body{background:var(--bg);font-family:"Arimo",Arial,sans-serif;position:relative;color:var(--text)}
.abs{position:absolute}
.logo{left:65px;top:34px;font-size:31px;font-weight:700;color:var(--white);letter-spacing:.5px}
.pill{height:22px;border-radius:11px;background:linear-gradient(var(--orange-light),var(--orange-dark));color:var(--white);font-size:11px;font-weight:700;letter-spacing:1px;display:flex;align-items:center;justify-content:center}
.signup{left:770px;top:22px;width:87px}
.login{left:872px;top:22px;width:88px}
.navbar{left:0;top:99px;width:1016px;height:32px;background:var(--bar);border-bottom:2px solid #3a3c40}
.nav{top:103px;font-size:15px;color:var(--nav)}
.nav.active{color:var(--orange-light)}
.search{left:749px;top:104px;width:214px;height:19px;border-radius:10px;background:var(--white)}
.stage{left:0;top:133px;width:1016px;height:322px;background:linear-gradient(var(--orange),var(--orange-dark))}
.photo{left:47px;top:136px;width:922px;height:317px;border:3px solid var(--white);background:linear-gradient(120deg,#d8dde3,#9fb6cf 45%,#e8e4de)}
.arrow{top:147px;width:29px;height:25px;background:var(--orange);display:flex;align-items:center;justify-content:center}
.arrow.prev{left:897px;border-radius:12px 0 0 12px}
.arrow.next{left:929px;border-radius:0 12px 12px 0}
.strap{left:0;top:455px;width:1016px;height:89px;background:linear-gradient(var(--orange-light),var(--orange-dark))}
.kicker{left:114px;top:477px;font-size:17px;font-weight:700;color:var(--black);letter-spacing:.5px;white-space:nowrap}
.tagline{left:58px;top:500px;width:620px;font-family:"Michroma",sans-serif;font-size:30px;font-variant:small-caps;color:var(--white);letter-spacing:0;white-space:nowrap;line-height:36px}
.newsletter{left:686px;top:467px;width:286px;height:66px;border-radius:10px;background:var(--black)}
.newsletter h3{position:absolute;left:15px;top:7px;font-size:17px;color:var(--white);font-weight:400}
.newsletter .field{position:absolute;left:16px;top:36px;width:237px;height:21px;border-radius:10px 0 0 10px;background:#e4e6e9;font-size:11px;color:var(--muted);padding:4px 12px}
.newsletter .go{position:absolute;left:236px;top:36px;width:34px;height:21px;border-radius:0 10px 10px 0;background:var(--orange);color:var(--white);font-size:12px;font-weight:700;display:flex;align-items:center;justify-content:center}
.card{width:313px;height:211px;border-radius:8px;background:linear-gradient(var(--white),#e9ebee);overflow:hidden}
.card-head{height:42px;background:linear-gradient(var(--orange-light),var(--orange-dark));border-radius:8px 8px 12px 12px;color:var(--white);font-size:18px;letter-spacing:1px;padding:11px 16px}
.plus{position:absolute;right:10px;top:9px}
.badge{position:absolute;left:8px;top:52px;width:99px;height:99px;border-radius:50%;border:5px solid #2a2a2c;background:radial-gradient(circle at 45% 35%,var(--orange-light),var(--orange-dark))}
.features{position:absolute;left:115px;top:62px;list-style:none;font-size:11.5px;line-height:20px;color:var(--text);width:190px}
.features li{padding-left:13px;position:relative}
.features li::before{content:"›";position:absolute;left:0;color:var(--orange);font-weight:700}
.register{position:absolute;right:12px;top:161px;width:130px;height:33px;border-radius:16px;background:linear-gradient(#f3f4f6,#d7dadd);color:var(--orange-dark);font-size:13px;font-weight:700;padding:9px 0 0 8px}
.register span{position:absolute;right:0;top:0;width:27px;height:33px;background:var(--orange);border-radius:0 16px 16px 0;color:var(--white);font-size:18px;text-align:center;line-height:31px}
.sidebar{left:704px;top:560px;width:266px;height:520px;border-radius:9px;background:var(--panel);overflow:hidden}
.sidebar .card-head{height:44px;font-size:17px;padding:12px 16px}
.sidebar h2{position:absolute;left:17px;top:56px;width:235px;font-size:16.5px;line-height:22px;color:#8a8d92;font-weight:700;border-bottom:2px dotted #b0b3b7;padding-bottom:4px}
.news{position:absolute;left:14px;top:130px;width:240px;list-style:none}
.news li{font-size:11px;line-height:15px;color:#8a8d92;padding:3px 0 8px 14px;border-bottom:1px dotted #aeb1b5;margin-bottom:2px;position:relative}
.news li::before{content:"›";position:absolute;left:2px;top:1px;color:var(--orange);font-weight:700;font-size:14px}
.readmore{position:absolute;left:0;bottom:0;width:266px;height:26px;background:var(--orange);color:var(--white);font-size:11px;letter-spacing:1px;text-align:right;padding:7px 14px}
.social{left:47px;top:1012px;width:638px;height:68px;border-radius:8px;background:linear-gradient(var(--white),#e4e6e9)}
.social .follow{position:absolute;left:9px;top:18px;font-size:12px;font-weight:700;color:var(--orange);line-height:16px;text-align:center}
.social p{position:absolute;left:110px;top:18px;font-size:12px;line-height:16px;color:#555}
.net{position:absolute;top:9px;width:50px;height:50px;border-radius:9px;background:#5a5d62;color:var(--white);font-size:11px;display:flex;align-items:center;justify-content:center}
.footer{left:47px;top:1112px;width:923px;height:50px;border-radius:6px;background:var(--bar);overflow:hidden}
.footer .links{position:absolute;left:18px;top:18px;font-size:11.5px;color:#c4c6ca;letter-spacing:.5px}
.footer .copy{position:absolute;left:638px;top:0;width:285px;height:50px;background:var(--orange);color:var(--white);font-size:11.5px;padding:18px 10px}
</style>
</head>
<body>
<header>
  <div class="abs logo">Vela-Q-Gauge</div>
  <a class="abs pill signup">SIGN UP!</a>
  <a class="abs pill login">LOGIN</a>
</header>
<nav>
  <div class="abs navbar"></div>
  <span class="abs nav active" style="left:70px">Home</span>
  <span class="abs nav" style="left:146px">What?</span>
  <span class="abs nav" style="left:229px">Why?</span>
  <span class="abs nav" style="left:305px">Demo</span>
  <span class="abs nav" style="left:381px">Reports</span>
  <span class="abs nav" style="left:483px">Blog</span>
  <span class="abs nav" style="left:559px">Pricing</span>
  <span class="abs nav" style="left:653px">Contact</span>
  <div class="abs search"></div>
</nav>
<section>
  <div class="abs stage"></div>
  <div class="abs photo" role="img" aria-label="Photo of a team of smiling young professionals working together at a laptop"></div>
  <div class="abs arrow prev"><svg width="10" height="12"><path d="M7 1 2 6l5 5" fill="none" stroke="#2a1a10" stroke-width="2"/></svg></div>
  <div class="abs arrow next"><svg width="10" height="12"><path d="M3 1l5 5-5 5" fill="none" stroke="#fff" stroke-width="2"/></svg></div>
  <div class="abs strap"></div>
  <div class="abs kicker">DEMAND GENERATION,SOCIAL ENGAGEMENT AND</div>
  <div class="abs tagline">Advocacy Marketing Platform</div>
  <div class="abs newsletter">
    <h3>Subscribe for Newsletter</h3>
    <div class="field">Enter email</div>
    <div class="go">GO</div>
  </div>
</section>

<main>
  <article class="abs card" style="left:47px;top:564px">
    <div class="card-head">ADVERTISERS</div>
    <svg class="plus" width="20" height="20"><circle cx="10" cy="10" r="9" fill="#fff"/><path d="M10 5v10M5 10h10" stroke="#e8561a" stroke-width="2.5"/></svg>
    <div class="badge" role="img" aria-label="Megaphone icon"></div>
    <ul class="features"><li>Create polls and surveys</li><li>Create Competitions</li><li>Create B2B and B2C demand generation campaigns</li></ul>
    <a class="register">Register Now!<span>›</span></a>
  </article>
  <article class="abs card" style="left:372px;top:564px">
    <div class="card-head">ADVOCATES</div>
    <svg class="plus" width="20" height="20"><circle cx="10" cy="10" r="9" fill="#fff"/><path d="M10 5v10M5 10h10" stroke="#e8561a" stroke-width="2.5"/></svg>
    <div class="badge" role="img" aria-label="Person holding a puzzle piece icon"></div>
    <ul class="features"><li>Create polls and surveys</li><li>Create Competitions</li><li>Create B2B and B2C demand generation campaigns</li></ul>
    <a class="register">Register Now!<span>›</span></a>
  </article>
  <article class="abs card" style="left:47px;top:787px">
    <div class="card-head">AFFILITES</div>
    <svg class="plus" width="20" height="20"><circle cx="10" cy="10" r="9" fill="#fff"/><path d="M10 5v10M5 10h10" stroke="#e8561a" stroke-width="2.5"/></svg>
    <div class="badge" role="img" aria-label="Two people meeting at a table icon"></div>
    <ul class="features"><li>Create polls and surveys</li><li>Create Competitions</li><li>Create B2B and B2C demand generation campaigns</li></ul>
    <a class="register">Register Now!<span>›</span></a>
  </article>
  <article class="abs card" style="left:372px;top:787px">
    <div class="card-head">AGENCIES</div>
    <svg class="plus" width="20" height="20"><circle cx="10" cy="10" r="9" fill="#fff"/><path d="M10 5v10M5 10h10" stroke="#e8561a" stroke-width="2.5"/></svg>
    <div class="badge" role="img" aria-label="Presentation board with rising chart icon"></div>
    <ul class="features"><li>Create polls and surveys</li><li>Create Competitions</li><li>Create B2B and B2C demand generation campaigns</li></ul>
    <a class="register">Register Now!<span>›</span></a>
  </article>

  <aside class="abs sidebar">
    <div class="card-head">VELA - Q - GAUGE.COM</div>
    <h2>LOREM IPSUM DOLOR SIT AMET, CSECTETUER ADIPISCING ELIT.</h2>
    <ul class="news">
      <li>Lorem ipsum dolor sit amet, csectetuer adipiscing elit. Aeneanmodo ligula eget dolor. Aenean massa.</li>
      <li>Lorem ipsum dolor sit amet, csectetuer adipiscing elit. Aeneanmodo ligula eget dolor. Aenean massa.</li>
      <li>Lorem ipsum dolor sit amet, csectetuer adipiscing elit. Aeneanmodo ligula eget dolor. Aenean massa.</li>
      <li>Lorem ipsum dolor sit amet, csectetuer adipiscing elit. Aeneanmodo ligula eget dolor. Aenean massa.</li>
      <li>Lorem ipsum dolor sit amet, csectetuer adipiscing elit. Aeneanmodo ligula eget dolor. Aenean massa.</li>
      <li>Lorem ipsum dolor sit amet, csectetuer adipiscing elit. Aeneanmodo ligula eget dolor. Aenean massa.</li>
    </ul>
    <div class="readmore">[ READ MORE ]</div>
  </aside>

  <section class="abs social">
    <div class="follow">FOLLOW US ON<br>SOCIAL MEDIA!</div>
    <p>Catch up with the latest news and information<br>from VELA - Q - Gauge.com on Social media.</p>
    <a class="net" style="left:375px">chirvo</a>
    <a class="net" style="left:441px">quillnest</a>
    <a class="net" style="left:507px">pormbly</a>
    <a class="net" style="left:573px">yammo</a>
  </section>
</main>

<footer class="abs footer">
  <div class="links">About Us &nbsp;|&nbsp; Contact Us &nbsp;|&nbsp; Sitemap &nbsp;|&nbsp; Privacy Policy</div>
  <div class="copy">2010 © VELA - Q - Gauge.com. All rights reserved.</div>
</footer>
</body>
</html>
```